VORLEN Website Design

We need a website designed for our company VORLEN. We are a luxury lifestyle club that will provide benefits and services for our members. The site should be clean & sleek, preferably using black and white (or darker colors). (example sites: brimvale.example, tusko.example)

Here is a link of a sample page I did using wix. (https://pelmundry4.sitebuild.example/mypage) This can be used to get a general idea.

Target Market(s)

Upper Middle Class in the United States

Number of Pages Required

5+ page

Font styles to use
Sans Serif
Other font styles liked:
• Arial (or other similar fonts)

Requirements
Must have
• A clean design that is eye-catching and speaks to our company.
Nice to have
• Ideas for copy.

```html
<!DOCTYPE html>
<html lang="en">
<head>
<meta charset="utf-8">
<title>VORLEN — A Members Only Lifestyle Club</title>
<link href="https://fonts.googleapis.com/css2?family=Arimo:wght@400;700&display=swap" rel="stylesheet">
<style>
:root{
  --ink:#111111;
  --dark:#222222;
  --paper:#ffffff;
  --mist:#f0f0f0;
  --grey:#555555;
  --line:#333333;
  --sky-top:#6f8192;
  --sky-mid:#c9d3dc;
  --sky-low:#eef1f4;
}
*{margin:0;padding:0;box-sizing:border-box}
html,body{width:1200px;height:3789px;overflow:hidden}
body{position:relative;background:var(--paper);color:var(--ink);font-family:"Arimo",Arial,sans-serif}
.abs{position:absolute}
.center{left:0;width:1200px;text-align:center}

/* nav */
.brand{left:40px;top:22px;font-size:30px;font-weight:700;letter-spacing:1px;color:var(--ink)}
.nav{left:424px;top:30px;display:flex;gap:30px;font-size:14px}
.nav span{color:var(--ink)}
.util{right:40px;top:30px;display:flex;gap:28px;font-size:14px;align-items:center}
.util span{display:flex;gap:6px;align-items:center}

/* hero */
.hero{left:0;top:0;width:1200px;height:695px;background:linear-gradient(180deg,var(--sky-top) 0%,var(--sky-mid) 45%,var(--sky-low) 100%)}
.hero-sub{left:90px;top:312px;font-size:27px;font-weight:700;line-height:1}
.hero-title{left:88px;top:338px;font-size:48px;font-weight:700;letter-spacing:1px;line-height:1}
.hero-copy{left:90px;top:391px;font-size:13px;line-height:1;color:var(--dark)}
.hero-btn{left:88px;top:424px;width:166px;height:45px;border:2px solid var(--ink);border-radius:24px;font-size:13px;display:flex;align-items:center;justify-content:center}
.dots{left:556px;top:642px;display:flex;gap:12px;align-items:center}
.dots i{width:8px;height:8px;border-radius:50%;background:var(--ink);display:block}
.dots i.on{width:18px;height:18px;background:none;border:2px solid var(--ink)}

/* shared */
.section-title{font-size:27px;font-weight:700;letter-spacing:1px}
.rule{left:555px;width:90px;height:3px;background:var(--ink)}
.pill-btn{width:166px;height:45px;border:2px solid var(--ink);border-radius:24px;font-size:12px;display:flex;align-items:center;justify-content:center;background:var(--paper)}

/* services */
.service-photo{top:841px;width:364px;height:447px}
.service-tag{top:1268px;height:52px;border-radius:26px;background:var(--ink);color:var(--paper);font-size:18px;font-weight:700;display:flex;align-items:center;justify-content:center}

/* about */
.about{left:0;top:1498px;width:600px;height:364px;background:var(--mist)}
.member-panel{left:600px;top:1498px;width:600px;height:364px;background:var(--dark);color:var(--paper)}
.panel-title{font-size:27px;font-weight:400;line-height:1}
.panel-copy{font-size:12.5px;line-height:20px;color:var(--grey)}
.panel-copy.light{line-height:25px;color:#e0e0e0}

/* newsletter */
.news-photo{top:2031px;width:364px;height:359px}
.news-card{top:2424px;width:330px}
.news-cat{font-size:12px;margin-bottom:14px}
.news-head{font-size:13px;font-weight:700;line-height:18px;margin-bottom:10px}
.news-copy{font-size:12px;line-height:19px;color:var(--dark)}
.news-more{margin-top:8px;display:flex;gap:6px}
.news-more i{display:block;width:6px;height:6px;border-radius:50%;background:var(--ink)}

/* contact */
.contact{left:0;top:2748px;width:1200px;height:493px;background:var(--mist)}
.field{height:32px;border-bottom:2px solid var(--line);font-size:12px;font-style:italic;color:var(--dark);padding-top:8px}

/* subscribe */
.subscribe-copy{font-size:17px;font-weight:700;line-height:24px;letter-spacing:.3px}
.email-box{left:366px;top:3383px;width:334px;height:44px;border:2px solid var(--ink);border-radius:22px;font-size:12px;font-style:italic;padding:13px 24px}
.send-btn{left:706px;top:3383px;width:134px;height:44px;border-radius:22px;background:var(--ink);color:var(--paper);font-size:13px;display:flex;align-items:center;justify-content:center}

/* footer */
.footer{left:0;top:3511px;width:1200px;height:278px;background:var(--dark);color:var(--paper)}
.footer-brand{font-size:40px;font-weight:700;letter-spacing:2px}
.footer-nav{left:0;width:1200px;display:flex;justify-content:center;gap:30px;font-size:13px}
.social{left:0;width:1200px;display:flex;justify-content:center;gap:30px}
.social i{display:block;width:16px;height:16px;border-radius:50%;background:var(--paper)}
.footer-rule{left:40px;width:1120px;height:1px;background:#777}
.copyright{font-size:12px}
</style>
</head>
<body>

<div class="abs hero" role="img" aria-label="Private jet flying above a sea of white clouds"></div>

<div class="abs brand">VORLEN</div>
<div class="abs nav"><span>Home</span><span>About</span><span>Services &amp; Benifits</span><span>Noted</span><span>Contact</span></div>
<div class="abs util">
  <span><svg width="14" height="14" viewBox="0 0 14 14"><circle cx="7" cy="7" r="6" fill="none" stroke="#111" stroke-width="1.4"/><path d="M1 7h12M7 1c3 3 3 9 0 12M7 1c-3 3-3 9 0 12" fill="none" stroke="#111" stroke-width="1"/></svg>EN</span>
  <span><svg width="12" height="12" viewBox="0 0 12 12"><path d="M2 10L10 2M4 2h6v6" fill="none" stroke="#111" stroke-width="1.6"/></svg>Login</span>
</div>

<div class="abs hero-sub">A MEMBERS ONLY</div>
<div class="abs hero-title">LIFESTYLE CLUB</div>
<div class="abs hero-copy">Lorem Ipsum is simply dummy text of the printing and typesetting industry.</div>
<div class="abs hero-btn">Learn More</div>
<div class="abs dots"><i class="on"></i><i></i><i></i><i></i></div>

<!-- services -->
<div class="abs center section-title" style="top:744px">SERVICES &amp; BENIFTS</div>
<div class="abs rule" style="top:799px"></div>

<div class="abs service-photo" style="left:40px;background:linear-gradient(160deg,#f4f4f4,#9aa4ad 60%,#3c4248)" role="img" aria-label="Hand with pencil using a calculator"></div>
<div class="abs service-photo" style="left:419px;background:linear-gradient(180deg,#cfd6dc,#a9b0b6 50%,#2b2d30)" role="img" aria-label="Black car parked beside a private jet"></div>
<div class="abs service-photo" style="left:798px;background:linear-gradient(160deg,#eceae6,#b9a58a 55%,#5a4634)" role="img" aria-label="Gavel and scales of justice on a desk with hand signing a document"></div>

<div class="abs service-tag" style="left:90px;width:272px">ACCOUNTING SERVICES</div>
<div class="abs service-tag" style="left:470px;width:270px">PRIVATE JET TRAVEL</div>
<div class="abs service-tag" style="left:839px;width:272px">LAWYER SERVICES</div>

<div class="abs pill-btn" style="left:517px;top:1385px">View All Services</div>

<!-- about -->
<div class="abs about"></div>
<div class="abs panel-title" style="left:40px;top:1564px">ABOUT US</div>
<div class="abs panel-copy" style="left:40px;top:1620px;width:503px;text-align:justify">Lorem Ipsum is simply dummy text of the printing and typesetting industry. Lorem Ipsum has been the industry's standard dummy text ever since the 1500s, when an unknown printer took a galley of type and scrambled it to make a type specimen book. It has survived not only five centuries, but also the leap into electronic typesetting, remaining essentially unchanged.</div>
<div class="abs pill-btn" style="left:40px;top:1753px;background:none">Read More</div>

<div class="abs member-panel"></div>
<div class="abs panel-title" style="left:652px;top:1564px;color:#fff">WE ARE VORLEN</div>
<div class="abs panel-copy light" style="left:652px;top:1618px;width:510px">Built in the image of a "Multi Family Office", VORLEN provides members with access to just about any service, experience, and event desirable.<br>VORLEN is truly the most exclusive lifestyle club out there.</div>
<div class="abs pill-btn" style="left:652px;top:1753px;background:none;border-color:#fff;color:#fff">Apply For Membership</div>

<!-- newsletter -->
<div class="abs center section-title" style="top:1928px">NEWSLETTER</div>
<div class="abs rule" style="top:1982px"></div>

<div class="abs news-photo" style="left:40px;background:linear-gradient(180deg,#f2f5f8,#b8c6d2 55%,#4a4e52)" role="img" aria-label="Couple with suitcases looking out an airport window"></div>
<div class="abs news-photo" style="left:419px;background:linear-gradient(160deg,#2f5b3a,#2aa6b9 45%,#d9cfb4 75%,#4d6b3a)" role="img" aria-label="Aerial view of a turquoise bay with sandy beach"></div>
<div class="abs news-photo" style="left:798px;background:linear-gradient(170deg,#2a0b3f,#7a2a9a 50%,#d14a86 80%,#3a0f48)" role="img" aria-label="Banquet hall lit in purple for an evening event"></div>

<div class="abs news-card" style="left:60px">
  <div class="news-cat">Lifestyle, Travel</div>
  <div class="news-head">HOW ASHGROVE CLUB'S REVAMP<br>HAS ELEVATED THE GOLFING LIFESTYLE</div>
  <div class="news-copy">Lorem Ipsum is simply dummy text of the printing and typesetting industry. Lorem Ipsum has been the industry's standard dummy text ever since the 1500s.</div>
  <div class="news-more"><i></i><i></i><i></i></div>
</div>
<div class="abs news-card" style="left:436px">
  <div class="news-cat">Lifestyle, Travel</div>
  <div class="news-head">HOW ASHGROVE CLUB'S REVAMP<br>HAS ELEVATED THE GOLFING LIFESTYLE</div>
  <div class="news-copy">Lorem Ipsum is simply dummy text of the printing and typesetting industry. Lorem Ipsum has been the industry's standard dummy text ever since the 1500s.</div>
  <div class="news-more"><i></i><i></i><i></i></div>
</div>
<div class="abs news-card" style="left:812px">
  <div class="news-cat">Lifestyle, Travel</div>
  <div class="news-head">HOW ASHGROVE CLUB'S REVAMP<br>HAS ELEVATED THE GOLFING LIFESTYLE</div>
  <div class="news-copy">Lorem Ipsum is simply dummy text of the printing and typesetting industry. Lorem Ipsum has been the industry's standard dummy text ever since the 1500s.</div>
  <div class="news-more"><i></i><i></i><i></i></div>
</div>

<div class="abs pill-btn" style="left:517px;top:2638px">View All</div>

<!-- contact -->
<div class="abs contact"></div>
<div class="abs center section-title" style="top:2818px">CONTACT US</div>
<div class="abs rule" style="top:2873px"></div>
<div class="abs field" style="left:268px;top:2946px;width:207px">Name</div>
<div class="abs field" style="left:495px;top:2946px;width:207px">Email Address</div>
<div class="abs field" style="left:722px;top:2946px;width:210px">Phone Number</div>
<div class="abs field" style="left:268px;top:3016px;width:664px">Massage</div>
<div class="abs pill-btn" style="left:517px;top:3110px;background:none">Submit</div>

<!-- subscribe -->
<div class="abs center subscribe-copy" style="top:3307px">SUBSCRIBE TO THE LATEST NEWS AND EXPERIENCES IN<br>GLOBAL LUXURY, CONTEMPORARY CULTURE, AND EXCLUSIVE OFFERS</div>
<div class="abs email-box">Email Address</div>
<div class="abs send-btn">Send</div>

<!-- footer -->
<div class="abs footer"></div>
<div class="abs center footer-brand" style="top:3547px;color:#fff">VORLEN</div>
<div class="abs footer-nav" style="top:3609px;color:#fff"><span>Home</span><span>About</span><span>Services &amp; Benifits</span><span>Noted</span><span>Contact</span></div>
<div class="abs social" style="top:3660px"><i></i><i></i><i></i><i></i><i></i></div>
<div class="abs footer-rule" style="top:3713px"></div>
<div class="abs center copyright" style="top:3740px;color:#fff">© Copyright 2018 Vorlen. All Right Reserved</div>

</body>
</html>
```